Corporate Two Sided Business Card

Looking for a Corporate "edgy" Modern look and feel for a business card

We are looking at two options. Dark background with our logo on it, white background with our logo on it - The background is more - Charcoal / Graphite then black

Details will be

Rosalind Tebb

Licensee / Director

m. 0452 918 604

e. rosalind@quarvelhome.com.au

quarvelhome.com.au

Target Market(s)

Professional Business people that refer use business and clients that own Investment Properties

Industry/Entity Type

Business

Contact Information for Business Card

Details will be

Rosalind Tebb

Licensee / Director

m. 0452 918 604

quarvelhome.com.au

Font styles to use
Serif

Colors
000000
ec1f27
eeeeee
ffffff

Requirements
Must have
• Two options - White Background and Dark Background. - Two sided
Nice to have
• A design that is edgy, modern and new to look instead of boring style corporate cards - It should be a full integrated design
Should not have
• Block looking - Cheap.

```html
<!DOCTYPE html>
<html lang="en">
<head>
<meta charset="utf-8">
<title>Quarvelhome Business Card</title>
<link href="https://fonts.googleapis.com/css2?family=Montserrat:wght@500;600&family=Nunito+Sans:wght@400;600&display=swap" rel="stylesheet">
<style>
  :root {
    --charcoal: #464646;
    --graphite-text: #4a4a4a;
    --red: #ec1f27;
    --white: #ffffff;
    --stage: #2e2e2e;
    --muted: #5a5a5a;
  }
  * { box-sizing: border-box; margin: 0; padding: 0; }
  html, body { width: 1200px; height: 864px; overflow: hidden; }
  body {
    background: var(--stage);
    display: flex;
    align-items: center;
    justify-content: center;
    gap: 40px;
    font-family: "Nunito Sans", sans-serif;
  }
  .card {
    width: 540px;
    height: 310px;
    position: relative;
    box-shadow: 0 10px 30px rgba(0,0,0,0.45);
  }
  .card--back {
    background: var(--charcoal);
    display: flex;
    flex-direction: column;
    align-items: center;
    justify-content: center;
  }
  .brand {
    display: flex;
    align-items: center;
    gap: 10px;
    font-family: "Montserrat", sans-serif;
    font-weight: 600;
    letter-spacing: 0.5px;
  }
  .brand__mark {
    width: 14px;
    height: 14px;
    background: var(--red);
  }
  .card--back .brand { color: var(--white); font-size: 50px; margin-top: 10px; }
  .card--back .brand__mark { width: 22px; height: 22px; }
  .card--back .web {
    position: absolute;
    bottom: 52px;
    color: var(--white);
    font-size: 15px;
    letter-spacing: 0.8px;
  }
  .card--front {
    background: var(--white);
    display: flex;
    align-items: center;
    padding: 0 0 0 34px;
  }
  .card--front .brand { color: var(--graphite-text); font-size: 29px; }
  .divider {
    width: 2px;
    height: 130px;
    background: var(--red);
    margin: 0 22px 0 18px;
  }
  .contact__name {
    font-family: "Montserrat", sans-serif;
    font-weight: 600;
    color: var(--red);
    font-size: 22px;
    line-height: 1.1;
  }
  .contact__role {
    color: var(--muted);
    font-size: 14px;
    margin-top: 2px;
    margin-bottom: 18px;
    letter-spacing: 0.3px;
  }
  .contact__list { list-style: none; }
  .contact__list li {
    display: flex;
    align-items: center;
    gap: 8px;
    color: var(--graphite-text);
    font-size: 14px;
    line-height: 1.45;
  }
  .contact__list svg { width: 12px; height: 12px; flex: none; }
</style>
</head>
<body>
  <section class="card card--back" aria-label="Card back, dark">
    <div class="brand"><span class="brand__mark"></span>quarvelhome</div>
    <p class="web">www.quarvelhome.com.au</p>
  </section>

  <section class="card card--front" aria-label="Card front, white">
    <div class="brand"><span class="brand__mark"></span>quarvelhome</div>
    <div class="divider"></div>
    <div class="contact">
      <p class="contact__name">Rosalind Tebb</p>
      <p class="contact__role">Licensee / Director</p>
      <ul class="contact__list">
        <li>
          <svg viewBox="0 0 12 12" aria-hidden="true"><rect x="3" y="0.8" width="6" height="10.4" rx="1.2" fill="none" stroke="#ec1f27" stroke-width="1.3"/><circle cx="6" cy="9.3" r="0.7" fill="#ec1f27"/></svg>
          0452 918 604
        </li>
        <li>
          <svg viewBox="0 0 12 12" aria-hidden="true"><rect x="0.5" y="2.5" width="11" height="7" fill="#ec1f27"/><path d="M0.8 2.8 L6 7 L11.2 2.8" fill="none" stroke="#fff" stroke-width="1"/></svg>
          rosalind@quarvelhome.com.au
        </li>
        <li>
          <svg viewBox="0 0 12 12" aria-hidden="true"><circle cx="6" cy="6" r="5.2" fill="none" stroke="#ec1f27" stroke-width="1.2"/><ellipse cx="6" cy="6" rx="2.2" ry="5.2" fill="none" stroke="#ec1f27" stroke-width="1"/><path d="M1 6 H11" stroke="#ec1f27" stroke-width="1"/></svg>
          quarvelhome.com.au
        </li>
      </ul>
    </div>
  </section>
</body>
</html>
```